Veteran Owned General Contractor needs Bold New Business Cards

We are a service disabled veteran owned small business. We're a general contractor that specializes in excavation, underground utilities, site work, land clearing and demolition. We would like a fresh, simple, bold, new look for our business cards. We're open to ideas! We'd like to incorporate the following information on the card:

Company Name & Logo, Name of Person, Job Title, Office Phone, Fax, Cell Phone, Email Address, Website, SDVOSB

Our logo is included. We look forward to your thoughts.

Thank you!
Updates

Reason: Hello Due to the overwhelming response to this project, we are extending the deadline one time to allow for improved communication and feedback with the top candidates. We would like to thank everyone for their hard work and exceptional creativity! Thank you

Industry/Entity Type

Business

Contact Information for Business Card

Font styles to use
Sans Serif

Requirements
Nice to have
• As we are a veteran owned company, it would be nice to incorporate an American flag into the design. Maybe on the back?

```html
<!DOCTYPE html>
<html lang="en">
<head>
<meta charset="utf-8">
<title>Hardline Business Card</title>
<link rel="stylesheet" href="https://fonts.googleapis.com/css2?family=Archivo:ital,wdth,wght@0,62..125,100..900;1,62..125,100..900&display=swap">
<style>
  :root {
    --green: #6cbe45;
    --black: #000000;
    --white: #ffffff;
    --grey: #8a8a8c;
    --machine-light: #f1f1f1;
    --machine-mid: #e2e2e2;
  }
  html, body {
    margin: 0;
    padding: 0;
    width: 1200px;
    height: 667px;
    overflow: hidden;
    background: var(--white);
  }
  .card {
    position: relative;
    width: 1200px;
    height: 667px;
    background: var(--white);
    font-family: "Archivo", Arial, sans-serif;
    overflow: hidden;
  }
  .machine-art {
    position: absolute;
    left: 470px;
    top: 0;
    width: 660px;
    height: 463px;
    background: radial-gradient(ellipse at 55% 55%, var(--machine-mid) 0%, var(--machine-light) 55%, rgba(255,255,255,0) 80%);
  }
  .brand-square {
    position: absolute;
    left: 122px;
    top: 64px;
    width: 224px;
    height: 224px;
    background: var(--black);
    border: 9px solid var(--grey);
    border-radius: 30px;
    box-sizing: border-box;
  }
  .person {
    position: absolute;
    left: 410px;
    top: 92px;
  }
  .person-name {
    margin: 0;
    font-size: 74px;
    font-weight: 800;
    font-stretch: 110%;
    line-height: 1;
    color: var(--black);
    letter-spacing: 1px;
  }
  .person-title {
    margin: 14px 0 0;
    font-size: 66px;
    font-weight: 200;
    font-style: italic;
    line-height: 1;
    color: var(--black);
  }
  .company-name {
    position: absolute;
    left: 78px;
    top: 322px;
    margin: 0;
    font-size: 124px;
    font-weight: 900;
    font-stretch: 125%;
    line-height: 1;
    color: var(--green);
    letter-spacing: 2px;
  }
  .contact-band {
    position: absolute;
    left: 0;
    top: 463px;
    width: 1200px;
    height: 204px;
    background: var(--black);
  }
  .contact-list {
    position: absolute;
    top: 50px;
    margin: 0;
    padding: 0;
    list-style: none;
  }
  .contact-list.left { left: 88px; }
  .contact-list.right { left: 595px; }
  .contact-item {
    display: flex;
    align-items: center;
    height: 34px;
    margin-bottom: 1px;
    font-size: 25px;
    font-weight: 800;
    font-style: italic;
    font-stretch: 90%;
    color: var(--white);
    white-space: nowrap;
  }
  .contact-label {
    background: var(--white);
    color: var(--black);
    padding: 0 4px;
    line-height: 28px;
    margin-right: 12px;
  }
</style>
</head>
<body>
  <div class="card">
    <div class="machine-art" role="img" aria-label="Faint grey illustration of an excavator in the background"></div>

    <div class="brand-square"></div>

    <div class="person">
      <h1 class="person-name">JOHN SMITH</h1>
      <p class="person-title">JOB TITLE</p>
    </div>

    <p class="company-name">HARDLINE</p>

    <section class="contact-band">
      <ul class="contact-list left">
        <li class="contact-item"><span class="contact-label">OFFICE PHONE:</span>(123) 555-6666</li>
        <li class="contact-item"><span class="contact-label">CELL PHONE:</span>(123) 555-6666</li>
        <li class="contact-item"><span class="contact-label">FAX:</span>(123) 555-6666</li>
      </ul>
      <ul class="contact-list right">
        <li class="contact-item"><span class="contact-label">EMAIL ADRESS:</span>YOURMAIL@EMAIL.COM</li>
        <li class="contact-item"><span class="contact-label">WEBSITE:</span>YOURWEB.COM</li>
        <li class="contact-item"><span class="contact-label">SDVOSB:</span></li>
      </ul>
    </section>
  </div>
</body>
</html>
```